PawHush business card

Looking for a fun and cool biz card for a new company with patent pending products. I have products to help and protect dogs hearing. My colors are pantone blue and orange.
Updates

Please add tag line: Protect the ones you love...even your PawHushes!

Target Market(s)

Animal/Dog lovers!

Industry/Entity Type

Retail

Contact Information for Business Card

I'm looking for something simple yet fun with all the info included for biz cards

Colors
0555a3
f78f20

Requirements
Must have
• Logo
Nice to have
• name, website and email
Should not have
• phone number

```html
<!DOCTYPE html>
<html lang="en">
<head>
<meta charset="utf-8">
<title>PawHush business card</title>
<link rel="stylesheet" href="https://fonts.googleapis.com/css2?family=Roboto:wght@400;500;700;900&display=swap">
<style>
  :root {
    --orange-deep: #e4521b;
    --orange: #f26a21;
    --orange-light: #f78f20;
    --blue: #0555a3;
    --white: #ffffff;
    --paper: #f4f5f7;
    --backdrop: #e9e6e1;
  }
  * { margin: 0; padding: 0; box-sizing: border-box; }
  html, body {
    width: 912px; height: 1200px; overflow: hidden;
    background: var(--backdrop);
    font-family: "Roboto", sans-serif;
  }
  .sheet {
    width: 912px; height: 1200px;
    display: flex; flex-direction: column;
    align-items: center; justify-content: center; gap: 34px;
  }
  .card {
    position: relative;
    width: 600px; height: 343px;
    border-radius: 18px;
    overflow: hidden;
    box-shadow: 0 6px 18px rgba(0,0,0,0.18);
  }
  .card--orange {
    background: linear-gradient(135deg, var(--orange-light) 0%, var(--orange) 45%, var(--orange-deep) 100%);
    color: var(--white);
  }
  .card--white { background: var(--paper); }

  .wordmark {
    font-family: "Roboto", sans-serif;
    font-weight: 900;
    letter-spacing: -1px;
    line-height: 1;
    white-space: nowrap;
  }

  /* White side */
  .white-side .brand-row {
    position: absolute; left: 50%; top: 50%;
    transform: translate(-50%, -50%);
    display: flex; align-items: center; gap: 22px;
  }
  .white-side .brand-dot {
    width: 84px; height: 84px; border-radius: 50%;
    background: var(--orange); flex: none;
  }
  .white-side .wordmark { font-size: 84px; color: var(--blue); }

  /* Front: contact side */
  .front .wordmark {
    position: absolute; left: 44px; bottom: 62px;
    font-size: 76px; color: var(--white);
  }
  .front .tagline {
    position: absolute; left: 46px; bottom: 30px;
    font-size: 14px; font-weight: 500; letter-spacing: 0.2px;
    white-space: nowrap;
  }
  .contact {
    position: absolute; right: 40px; top: 40px;
    text-align: right;
  }
  .contact__name {
    font-weight: 700; font-size: 19px; letter-spacing: 0.5px; text-transform: uppercase;
  }
  .contact__title {
    font-size: 14px; font-weight: 400; margin-top: 3px; margin-bottom: 14px;
  }
  .contact__line {
    display: flex; justify-content: flex-end; align-items: center; gap: 8px;
    font-size: 14px; line-height: 1.55;
  }
  .contact__line svg { width: 11px; height: 11px; flex: none; fill: var(--white); }

  /* Back: logo side */
  .back .wordmark {
    position: absolute; left: 50%; top: 44%;
    transform: translate(-50%, -50%);
    font-size: 104px; color: var(--white);
  }
  .back .website {
    position: absolute; right: 92px; bottom: 70px;
    font-size: 16px; font-weight: 400; letter-spacing: 0.3px;
  }
</style>
</head>
<body>
<main class="sheet">

  <section class="card card--white white-side" aria-label="Card brand side">
    <div class="brand-row">
      <span class="brand-dot"></span>
      <p class="wordmark">PawHush</p>
    </div>
  </section>

  <section class="card card--orange front" aria-label="Card front with contact details">
    <div class="contact">
      <p class="contact__name">Daniel Carver</p>
      <p class="contact__title">Director</p>
      <p class="contact__line">118 Maple Grove Rd. Suite</p>
      <p class="contact__line">Oregon OR 97201</p>
      <p class="contact__line">hello@pawhush.com
        <svg viewBox="0 0 24 24" aria-hidden="true"><path d="M2 5h20v14H2zm2 2v.5l8 5 8-5V7zm0 2.8V17h16V9.8l-8 5z"/></svg>
      </p>
      <p class="contact__line">www.pawhush.com
        <svg viewBox="0 0 24 24" aria-hidden="true"><circle cx="12" cy="12" r="10"/></svg>
      </p>
    </div>
    <p class="wordmark">PawHush</p>
    <p class="tagline">Protect the ones you love...even your PawHushes!</p>
  </section>

  <section class="card card--orange back" aria-label="Card back with brand name">
    <p class="wordmark">PawHush</p>
    <p class="website">www.pawhush.com</p>
  </section>

</main>
</body>
</html>
```